Blue Heron IT Business Card - Clean, Simple

Need a simple, clean standard sized business card for an IT consulting business using existing logo and company colours. Background should be mainly white. Feel free to be creative but clean, simple, quiet design is preferred. Font is specified in logo but any sans serif fonts work.

Contact Information for card is as follows (doesn't need to be in this exact order):

Martin Calloway
Owner
martin@blueheronit.ca
705-391-2586
www.blueheronit.ca

Target Market(s)

Small to medium sized business.

Industry/Entity Type

IT Consulting

Contact Information for Business Card

Logo and contact info.

Font styles to use
Sans Serif

Colors
EE7325
F08F49
F5BC92
FAE3D3
FDF4ED

Requirements
Must have
• All white or mostly white background.

```html
<!DOCTYPE html>
<html lang="en">
<head>
<meta charset="utf-8">
<title>Blue Heron IT – Business Card</title>
<link rel="stylesheet" href="https://fonts.googleapis.com/css2?family=Montserrat:wght@500;700&display=swap">
<style>
  :root {
    --orange: #e0681f;
    --ink: #262626;
    --card: #ffffff;
    --backdrop: #eeeeee;
  }
  * { margin: 0; padding: 0; box-sizing: border-box; }
  html, body {
    width: 1200px; height: 801px; overflow: hidden;
    background: var(--backdrop);
    font-family: "Montserrat", Arial, sans-serif;
  }
  .card {
    position: absolute; left: 150px; top: 143px;
    width: 900px; height: 514px;
    background: var(--card);
    box-shadow: 0 6px 24px rgba(0,0,0,0.12);
  }
  .brand {
    position: absolute; left: 70px; top: 220px;
    display: flex; align-items: center; gap: 14px;
  }
  .brand-dot {
    width: 26px; height: 26px; border-radius: 50%;
    background: var(--orange);
  }
  .brand-name {
    font-weight: 500; font-size: 40px; color: var(--ink);
    letter-spacing: -0.5px; white-space: nowrap;
  }
  .divider {
    position: absolute; left: 455px; top: 160px;
    width: 2px; height: 200px; background: var(--ink);
  }
  .contact {
    position: absolute; left: 500px; top: 168px;
  }
  .person-name {
    font-weight: 700; font-size: 29px; color: var(--orange);
    letter-spacing: 0.5px; line-height: 1.1;
  }
  .person-role {
    font-weight: 500; font-size: 24px; color: var(--ink);
    margin-top: 4px;
  }
  .details { list-style: none; margin-top: 30px; }
  .details li {
    display: flex; align-items: center; gap: 18px;
    font-weight: 500; font-size: 19px; color: var(--ink);
    letter-spacing: 0.6px; height: 34px;
  }
  .icon { width: 22px; height: 22px; flex: none; }
</style>
</head>
<body>
  <div class="card">
    <div class="brand">
      <span class="brand-dot"></span>
      <span class="brand-name">Blue Heron IT</span>
    </div>

    <div class="divider"></div>

    <div class="contact">
      <p class="person-name">Martin Calloway</p>
      <p class="person-role">Owner</p>
      <ul class="details">
        <li>
          <svg class="icon" viewBox="0 0 22 22" aria-hidden="true">
            <circle cx="11" cy="11" r="11" fill="var(--orange)"/>
            <rect x="5.5" y="7.5" width="11" height="7.5" fill="none" stroke="#fff" stroke-width="1.3"/>
            <path d="M5.5 7.5 L11 12 L16.5 7.5" fill="none" stroke="#fff" stroke-width="1.3"/>
          </svg>
          <span>martin@blueheronit.ca</span>
        </li>
        <li>
          <svg class="icon" viewBox="0 0 22 22" aria-hidden="true">
            <circle cx="11" cy="11" r="11" fill="var(--orange)"/>
            <path d="M8 5.5 L10 8.5 L8.8 10 C9.5 11.6 10.5 12.6 12 13.3 L13.5 12 L16.5 14 L15.2 16.3 C10.5 16 6 11.5 5.8 6.8 Z" fill="#fff"/>
          </svg>
          <span>705-391-2586</span>
        </li>
        <li>
          <svg class="icon" viewBox="0 0 22 22" aria-hidden="true">
            <circle cx="11" cy="11" r="11" fill="var(--orange)"/>
            <g fill="none" stroke="#fff" stroke-width="1.1">
              <circle cx="11" cy="11" r="6"/>
              <ellipse cx="11" cy="11" rx="2.6" ry="6"/>
              <line x1="5" y1="11" x2="17" y2="11"/>
              <line x1="6" y1="8" x2="16" y2="8"/>
              <line x1="6" y1="14" x2="16" y2="14"/>
            </g>
          </svg>
          <span>www.blueheronit.ca</span>
        </li>
      </ul>
    </div>
  </div>
</body>
</html>
```